K7 Electrical Services Ltd Web design

I require a web site for my new electrical contracting company. We are customer service orientated. Offering high value electrical installations, design and maintenance. Focused on custom residential and commercial upgrading. Lighting design and application are paramount in our company's services. Industry leading product use and integration are always on the forefront with our customer client services. As well as energy efficiency.

Target Market(s)

Homebuilders, General Contractors, Property management companies, clients, individuals,

Industry/Entity Type

Electric Company

Coding

Coded - Design and coding required

Number of Pages Required

3 page

Requirements
Must have
• Classic, modern, edgy but not trendy . Appeals to the masse.
• 3 page
• home page
• about page
• gallery page
• ability to contact from the webiste
Nice to have
• open to all types of designs that are relative to the construction industry.
• Black, Grey, metallic ice blue and deep purple colours from the logo.
Should not have
• anything cheesy with cartoon light bulb images.

```html
<!DOCTYPE html>
<html lang="en">
<head>
<meta charset="utf-8">
<title>K7 Electrical Services Ltd</title>
<link href="https://fonts.googleapis.com/css2?family=Lato:wght@400;700&family=Play:wght@400;700&display=swap" rel="stylesheet">
<style>
:root{
  --purple:#5b2c8f;
  --purple-deep:#4a2277;
  --footer-purple:#6a3399;
  --ink:#222;
  --text:#444;
  --muted:#9a9a9a;
  --light:#f1f1f1;
  --white:#fff;
  --dark:#1d2226;
  --bar:#8c8c8c;
}
*{margin:0;padding:0;box-sizing:border-box}
html,body{width:1200px;height:3261px;overflow:hidden}
body{position:relative;font-family:"Lato",sans-serif;color:var(--text);background:var(--white)}
.abs{position:absolute}
.heading{font-family:"Play",sans-serif;font-weight:700;text-align:center;font-size:36px;color:var(--purple);letter-spacing:.5px}
.heading span{color:var(--muted);font-weight:400}
.rule{position:absolute;left:540px;width:120px;height:4px;background:linear-gradient(90deg,var(--purple) 0 60%,#c8c8c8 60% 100%)}
.brand{font-family:"Lato",sans-serif;font-weight:400;color:var(--ink);display:flex;align-items:center;gap:10px;letter-spacing:.5px;white-space:nowrap}
.brand i{display:block;width:12px;height:12px;background:var(--ink)}

/* header + hero */
.hero{left:0;top:0;width:1200px;height:554px;background:linear-gradient(170deg,#d9d4cc 0%,#b8aa98 35%,#8f7f6d 60%,#c9c2b8 100%)}
.site-header{left:0;top:0;width:1200px;height:108px;background:rgba(255,255,255,.88)}
.site-header .brand{position:absolute;left:141px;top:40px;font-size:24px}
.schedule-link{left:817px;top:14px;font-size:15px;font-weight:700;color:var(--ink)}
.nav a{position:absolute;top:64px;font-size:14px;font-weight:700;color:var(--ink);text-decoration:none}
.nav a.active{color:var(--purple)}
.hero-title{left:150px;top:268px;width:440px;text-align:center;font-size:29px;line-height:37px;font-weight:400;color:var(--white);text-shadow:0 2px 6px rgba(0,0,0,.6)}
.arrow-box{width:30px;height:28px;background:#222;display:flex;align-items:center;justify-content:center}
.hero-wave{left:0;top:470px}

/* intro */
.intro .brand{position:absolute;left:0;width:1200px;justify-content:center;top:612px;font-size:28px}
.intro-text{left:180px;top:684px;width:840px;text-align:center;font-size:15px;line-height:24px;color:var(--ink)}
.card{position:absolute;top:765px;width:283px;height:370px}
.card-photo{position:absolute;left:0;top:0;width:283px;height:257px;border-radius:4px 4px 0 0}
.card-body{position:absolute;left:18px;top:207px;width:248px;height:163px;background:var(--white);box-shadow:0 2px 8px rgba(0,0,0,.18);border-radius:3px;text-align:center;padding-top:20px}
.card-body h3{font-size:17px;line-height:22px;font-weight:700;color:var(--ink)}
.card-body p{font-size:12px;line-height:19px;color:var(--text);margin:6px 24px 0}
.btn-pill{display:inline-block;margin-top:10px;width:102px;height:25px;line-height:25px;border-radius:13px;background:var(--purple);color:var(--white);font-size:12px}
.card.featured .card-body{background:var(--purple)}
.card.featured h3,.card.featured p{color:var(--white)}
.card.featured .btn-pill{background:var(--white);color:var(--purple)}

/* about */
.about{left:0;top:1196px;width:1200px;height:384px;background:var(--light)}
.about-title{left:0;top:1244px;width:1200px;display:flex;justify-content:center;align-items:center;gap:16px}
.about-title b{font-family:"Play",sans-serif;font-size:36px;color:var(--purple)}
.about-title .brand{font-size:28px}
.about-copy{left:141px;width:918px;text-align:center;font-size:11.5px;line-height:20px;color:var(--text)}
.btn-call{left:489px;top:1489px;width:196px;height:44px;border-radius:6px;background:var(--purple);color:var(--white);font-weight:700;font-size:21px;text-align:center;line-height:44px;box-shadow:0 2px 0 var(--purple-deep)}

/* why choose */
.why{left:0;top:1580px;width:1200px;height:333px;background:linear-gradient(180deg,#2a3238 0%,#1c2125 45%,#0f1214 100%)}
.why-title{left:0;top:1645px;width:1200px;font-family:"Play",sans-serif;font-weight:700;font-size:36px;text-align:center;color:var(--purple)}
.why-title span{color:var(--white)}
.why-text{left:0;width:1200px;text-align:center;color:var(--white);font-size:16px;letter-spacing:.3px}
.why-cta{left:0;top:1798px;width:1200px;text-align:center;color:var(--white);font-size:15px;font-weight:700;line-height:22px}

/* gallery */
.gallery-title{left:0;top:1985px;width:1200px}
.tile{position:absolute}
.tile-note{position:absolute;left:491px;top:2061px;width:183px;height:130px;background:rgba(20,20,20,.75);color:var(--white);font-size:12px;line-height:17px;padding:30px 14px}
.video-bar{position:absolute;left:155px;top:2305px;width:310px;height:4px;background:rgba(255,255,255,.6)}
.video-bar::before{content:"";position:absolute;left:0;top:0;width:60px;height:4px;background:#e33}
.chev{position:absolute}

/* reviews */
.reviews{left:0;top:2417px;width:1200px;height:420px;background:var(--light)}
.reviews-title{left:0;top:2458px;width:1200px}
.review-photo{left:141px;top:2561px;width:255px;height:211px;border:3px solid var(--dark)}
.review-text{left:430px;top:2582px;width:629px;font-size:13.5px;line-height:25px;color:var(--text)}
.review-name{left:430px;top:2729px;font-family:"Play",sans-serif;font-size:14px;letter-spacing:1px;color:var(--text)}
.review-line{left:574px;top:2740px;width:485px;height:1px;background:#c8c8c8}

/* footer */
.footer{left:0;top:2837px;width:1200px;height:380px;background:var(--footer-purple)}
.inquiry{left:141px;top:2826px;width:337px;height:344px;background:var(--white);box-shadow:0 3px 10px rgba(0,0,0,.2)}
.inquiry h4{position:absolute;left:68px;top:34px;font-size:21px;font-weight:700;color:var(--ink)}
.inquiry h4 span{color:var(--purple)}
.field{position:absolute;left:42px;width:252px;height:34px;border:1px solid #d8d8d8;font-size:10px;color:#999;padding:11px 8px}
.submit{position:absolute;left:42px;top:274px;width:252px;height:31px;background:var(--purple);color:var(--white);font-weight:700;font-size:15px;text-align:center;line-height:31px;letter-spacing:.5px}
.footer-head{font-weight:700;font-size:15px;color:var(--white);letter-spacing:.3px}
.footer-line{height:1px;background:rgba(255,255,255,.35)}
.quick-links a{position:absolute;left:515px;color:var(--white);font-size:12.5px;text-decoration:none}
.social{position:absolute;top:3101px;width:26px;height:26px;border-radius:50%}
.contact-item{position:absolute;left:811px;color:var(--white);font-size:12.5px;line-height:18px}
.contact-icon{position:absolute;left:780px}
.bottom-bar{left:0;top:3217px;width:1200px;height:44px;background:var(--bar)}
.bottom-bar p{position:absolute;top:15px;font-size:11px;color:var(--white)}
</style>
</head>
<body>

<div class="abs hero" role="img" aria-label="Electrician on a ladder installing a chandelier in a bright living room"></div>
<header class="abs site-header">
  <div class="brand"><i></i>K7 Electrical Services Ltd</div>
</header>
<div class="abs schedule-link">SCHEDULE YOUR SERVICE TODAY</div>
<nav class="nav">
  <a class="active" style="left:637px">HOME</a>
  <a style="left:733px">ABOUT US</a>
  <a style="left:854px">GALLERY</a>
  <a style="left:961px">CONTACT US</a>
</nav>
<h1 class="abs hero-title">Offering High Value Electrical Installations, Design &amp; Maintenance</h1>
<div class="abs arrow-box" style="left:4px;top:270px"><svg width="10" height="12"><path d="M8 1 2 6l6 5z" fill="#fff"/></svg></div>
<div class="abs arrow-box" style="left:1166px;top:270px"><svg width="10" height="12"><path d="M2 1l6 5-6 5z" fill="#fff"/></svg></div>
<svg class="abs hero-wave" width="1200" height="90" viewBox="0 0 1200 90">
  <path d="M0 45 Q600 105 1200 40 L1200 90 L0 90Z" fill="#fff"/>
  <path d="M0 45 Q600 105 1200 40" fill="none" stroke="#5b2c8f" stroke-width="9"/>
</svg>

<section class="intro">
  <div class="brand"><i></i>K7 Electrical Services Ltd</div>
  <p class="abs intro-text">. We are customer service orientated. Offering high value text of the printing and typesetting industry. Lorem Ipsum has been the industry's standard dummy text ever since the 1500s.</p>

  <article class="card" style="left:141px">
    <div class="card-photo" role="img" aria-label="Multimeter testing wiring in an electrical panel" style="background:linear-gradient(135deg,#c9a33a,#8a5a2c 50%,#3d4a5a)"></div>
    <div class="card-body"><h3>Electrical<br>Installations</h3><p>Lorem ipsum dolor sit amet werew erer consectetuer adipiscing elit</p><span class="btn-pill">Read More</span></div>
  </article>
  <article class="card featured" style="left:459px">
    <div class="card-photo" role="img" aria-label="Electrician fitting a chandelier to a ceiling" style="background:linear-gradient(160deg,#e8e4de,#b9ad9c 60%,#8a7b68)"></div>
    <div class="card-body"><h3>Design<br>And Maintenance</h3><p>Lorem ipsum dolor sit amet werew erer consectetuer adipiscing elit</p><span class="btn-pill">Read More</span></div>
  </article>
  <article class="card" style="left:776px">
    <div class="card-photo" role="img" aria-label="Modern room lit by recessed ceiling lights" style="background:linear-gradient(180deg,#e6e2da,#a08770 55%,#5a4536)"></div>
    <div class="card-body"><h3>Lighting Design<br>And Application</h3><p>Lorem ipsum dolor sit amet werew erer consectetuer adipiscing elit</p><span class="btn-pill">Read More</span></div>
  </article>
</section>

<section class="abs about"></section>
<div class="abs about-title"><b>ABOUT</b><div class="brand"><i></i>K7 Electrical Services Ltd</div></div>
<div class="rule" style="top:1313px"></div>
<p class="abs about-copy" style="top:1328px">Lorem ipsum dolor sit amet, consectetuer adipiscing elit, sed diam nonummy nibh euismod tincidunt ut laoreet dolore magna aliquam erat volutpat. Ut wisi enim ad minim veniam, quis nostrud exerci tation ullamcorper suscipit lobortis nisl ut aliquip ex ea commodo consequat.</p>
<p class="abs about-copy" style="top:1372px">Lorem ipsum dolor sit amet, consectetuer adipiscing elit, sed diam nonummy nibh euismod tincidunt ut laoreet dolore magna aliquam erat volutpat. Ut wisi enim ad minim veniam, quis nostrud exerci tation ullamcorper suscipit lobortis nisl ut aliquip ex ea commodo consequat. Duis autem vel eum iriure dolor in hendrerit in vulputate velit esse molestie consequat, vel illum dolore eu feugiat nulla facilisis at vero eros et accumsan et iusto odio dignissim qui blandit praesent luptatum zzril delenit augue duis dolore te feugait nulla facilisi. Duis autem vel eum iriure dolor in hendrerit in vulputate velit esse molestie consequat, vel illum dolore eu feugiat nulla facilisis at vero eros et accumsan et iusto odio dignissim qui blandit praesent luptatum zzril delenit augue duis dolore te feugait nulla facilisi.</p>
<div class="abs btn-call">Call Us Today</div>

<section class="abs why" role="img" aria-label="Dusk view of a lit home interior and patio"></section>
<h2 class="abs why-title">WHY CHOOSE <span>US</span></h2>
<p class="abs why-text" style="top:1716px">Lighting design and application are paramount in our company's services.</p>
<p class="abs why-text" style="top:1751px">Industry leading product use &amp; integration are always on the forefront with our customer client services.</p>
<p class="abs why-cta">SCHEDULE<br>YOUR SERVICE TODAY</p>

<h2 class="abs heading gallery-title">WORK <span>GALLERY</span></h2>
<div class="rule" style="top:2033px"></div>
<svg class="chev" style="left:96px;top:2170px" width="22" height="56"><path d="M20 2 3 28l17 26" fill="none" stroke="#999" stroke-width="2"/></svg>
<svg class="chev" style="left:1082px;top:2170px" width="22" height="56"><path d="M2 2l17 26L2 54" fill="none" stroke="#999" stroke-width="2"/></svg>
<div class="tile" role="img" aria-label="Video of an electrician working on a fuse board" style="left:141px;top:2061px;width:339px;height:272px;background:linear-gradient(120deg,#3e5a86,#8da2b8 45%,#5e5a52)"></div>
<div class="video-bar"></div>
<div class="tile" role="img" aria-label="Workers on a construction site ceiling" style="left:491px;top:2061px;width:183px;height:130px;background:linear-gradient(160deg,#6b6460,#3a3532)"></div>
<div class="tile-note">Lorem ipsums is the dummy text of the industry is the dummy text of the.</div>
<div class="tile" role="img" aria-label="Electrician on a ladder in an unfinished timber frame room" style="left:491px;top:2202px;width:183px;height:131px;background:linear-gradient(160deg,#c49a6c,#7a5a3e)"></div>
<div class="tile" role="img" aria-label="Hands holding a voltage tester at a switchboard" style="left:685px;top:2061px;width:180px;height:272px;background:linear-gradient(170deg,#8c9198,#4b5059 55%,#c9a23a)"></div>
<div class="tile" role="img" aria-label="Electrician fitting a ceiling light" style="left:876px;top:2061px;width:183px;height:130px;background:linear-gradient(180deg,#e4dcd0,#a7876a)"></div>
<div class="tile" role="img" aria-label="Open plan office with pendant lighting" style="left:876px;top:2202px;width:183px;height:131px;background:linear-gradient(180deg,#d8cfc2,#9b8a77)"></div>

<section class="abs reviews"></section>
<h2 class="abs heading reviews-title">HAPPY CUSTOMER <span>REVIEWS</span></h2>
<div class="rule" style="top:2508px"></div>
<svg class="chev" style="left:96px;top:2640px" width="22" height="56"><path d="M20 2 3 28l17 26" fill="none" stroke="#777" stroke-width="2"/></svg>
<svg class="chev" style="left:1082px;top:2640px" width="22" height="56"><path d="M2 2l17 26L2 54" fill="none" stroke="#777" stroke-width="2"/></svg>
<div class="abs review-photo" role="img" aria-label="Family relaxing together in their living room" style="background:linear-gradient(160deg,#dfe3e6,#b9c3c9 50%,#8a7f74)"></div>
<p class="abs review-text">Lorem ipsum dolor sit amet, consectetuer adipiscing elit, sed diam nonummy nibh euismod tincidunt ut laoreet dolore magna aliquam erat volutpat. Ut wisi enim ad minim veniam, quis nostrud exerci tation ullamcorper suscipit lobortis nisl ut aliquip ex ea commodo consequat. Duis autem vel eum iriure dolor in sdghjlhendrerit in vulputate velit esse molestie consequat, vel illum dolore eu feugiat nulla facilisis at vero eros et.</p>
<p class="abs review-name">-DANIEL WHITMORE</p>
<div class="abs review-line"></div>

<footer class="abs footer"></footer>
<form class="abs inquiry">
  <h4>QUICK <span>INQUIRY</span></h4>
  <div class="field" style="top:87px">Name</div>
  <div class="field" style="top:126px">Phone</div>
  <div class="field" style="top:165px">Email</div>
  <div class="field" style="top:207px;height:54px">Message</div>
  <div class="submit">SUBMIT NOW</div>
</form>

<div class="abs footer-head" style="left:515px;top:2906px">QUICK LINKS</div>
<div class="abs footer-line" style="left:515px;top:2932px;width:215px"></div>
<nav class="quick-links">
  <a style="top:2947px">› Home</a>
  <a style="top:2973px">› About Us</a>
  <a style="top:2999px">› Gallery</a>
  <a style="top:3025px">› Contact Us</a>
</nav>
<div class="abs footer-head" style="left:515px;top:3062px">FOLLOW US TODAY</div>
<div class="abs footer-line" style="left:515px;top:3088px;width:215px"></div>
<span class="social" style="left:516px;background:#3b5998"></span>
<span class="social" style="left:551px;background:#1da1f2"></span>
<span class="social" style="left:587px;background:#0077b5"></span>
<span class="social" style="left:622px;background:#dd4b39"></span>
<span class="social" style="left:657px;background:#e4405f"></span>

<div class="abs footer-head" style="left:778px;top:2906px">CONTACT DETAILS</div>
<div class="abs footer-line" style="left:778px;top:2932px;width:282px"></div>
<svg class="contact-icon" style="top:2950px" width="16" height="20" viewBox="0 0 16 20"><path d="M8 1a6 6 0 0 0-6 6c0 5 6 12 6 12s6-7 6-12a6 6 0 0 0-6-6z" fill="none" stroke="#fff" stroke-width="1.5"/><circle cx="8" cy="7" r="2" fill="#fff"/></svg>
<p class="contact-item" style="top:2947px">123 Orem ipsum dolor sit amet,<br>consectetuer, NC-123456</p>
<svg class="contact-icon" style="top:2994px" width="18" height="18" viewBox="0 0 18 18"><path d="M4 1l3 4-2 2c1 2 3 4 5 5l2-2 4 3-2 3C8 16 2 10 1 4z" fill="none" stroke="#fff" stroke-width="1.4"/></svg>
<p class="contact-item" style="top:2991px">Phone<br>555-204-7190</p>
<svg class="contact-icon" style="top:3039px" width="18" height="14" viewBox="0 0 18 14"><rect x="1" y="1" width="16" height="12" fill="none" stroke="#fff" stroke-width="1.4"/><path d="M1 1l8 7 8-7" fill="none" stroke="#fff" stroke-width="1.4"/></svg>
<p class="contact-item" style="top:3033px">Email<br>inquiry@k7electricalservices.com</p>

<div class="abs bottom-bar">
  <p style="left:148px">Copyright © K7 Electrical Services Ltd - 2018. All Rights Reserved.</p>
  <p style="left:850px">Privacy Policy &nbsp;|&nbsp; Terms And Conditions</p>
</div>

</body>
</html>
```